Brisk Meadow Builders needs a product brochure

We need a new flyer for our Patio Perch Lounge. Here is some of the copy your will need.
"Turn your back yard into the ultimate entertianment venue with the stunning Patio Perch Lounge!"
"Entertain family & friends in your very own back yard!"
"Available with or without solar and comes in a variety of colors"
"The Patio Perch Lounge measures 5' deep by 10' wide and is 9'-6" at it's highest point"
"Constructed with treated 4x4's, primed then painted with Thornby Calder best exterior paint for years of care free enjoyment. Also, Marlow Pendt Keystead shingles are dimensional, have a 25 year warranty and are rated for 150 mph winds!"
"TV Mount included. Shelves and TV are sold separately"
There also needs to be a box where we can add the price into later. The price can change from time to time due to material cost fluctuation.
Look and feel
Each slider illustrates characteristics of the customer's brand and the style your logo design should communicate.

```html
<!DOCTYPE html>
<html lang="en">
<head>
<meta charset="utf-8">
<title>Patio Perch Lounge Flyer</title>
<link href="https://fonts.googleapis.com/css2?family=Anton&family=Open+Sans:wght@400;600;700&display=swap" rel="stylesheet">
<style>
:root{
  --stage:#e9e9e9;
  --wood-dark:#1c120b;
  --wood-mid:#3a2617;
  --gold:#f2c230;
  --gold-deep:#c8901a;
  --green:#7cc242;
  --cream:#f4ead8;
  --text:#e8e1d4;
  --panel:rgba(0,0,0,.45);
  --line:#c9a23a;
}
*{box-sizing:border-box;margin:0;padding:0}
html,body{width:878px;height:1200px;overflow:hidden;background:var(--stage);font-family:"Open Sans",Arial,sans-serif}
.spread{position:absolute;top:328px;left:10px;display:flex;gap:18px}
.page{width:420px;height:544px;position:relative;overflow:hidden;color:var(--text);
  background:repeating-linear-gradient(90deg,var(--wood-dark) 0 38px,#24170e 38px 40px,var(--wood-mid) 40px 78px,#22160d 78px 80px);
  box-shadow:0 6px 18px rgba(0,0,0,.25)}
.page::before{content:"";position:absolute;inset:0;background:radial-gradient(ellipse at 50% 35%,rgba(0,0,0,0) 30%,rgba(0,0,0,.55) 100%)}
.page>*{position:absolute}
.brand{top:12px;left:0;right:0;display:flex;justify-content:center;align-items:center;gap:6px;z-index:2}
.brand-dot{width:12px;height:12px;border-radius:50%;background:var(--green)}
.brand-name{font:700 11px "Open Sans",Arial,sans-serif;color:var(--green);letter-spacing:.5px}
.photo{border:2px solid var(--line);z-index:1}
.shelf{top:38px;left:40px;width:340px;height:196px;background:linear-gradient(180deg,#4a3520,#2b1d12 55%,#5b4026)}
.chain{top:0;width:2px;height:40px;background:repeating-linear-gradient(180deg,#aaa 0 3px,#555 3px 5px);z-index:1}
.thumbs{top:244px;left:40px;width:340px;display:flex;gap:6px;z-index:1}
.thumb{flex:1;height:50px;border:2px solid var(--line)}
.t1{background:linear-gradient(135deg,#6b8a4c,#3c2a1c)}
.t2{background:linear-gradient(135deg,#8fa7b8,#4a3522)}
.t3{background:linear-gradient(135deg,#5c6d3a,#2f2a20)}
.t4{background:linear-gradient(135deg,#9a6a3c,#3a2616)}
.tagline{top:300px;left:30px;right:30px;text-align:center;font:600 11px/1.3 "Open Sans",Arial,sans-serif;color:var(--cream);z-index:2}
.title{top:333px;left:40px;font:32px/1 "Anton",Impact,sans-serif;color:var(--gold);letter-spacing:1px;z-index:2;white-space:nowrap}
.seal{top:326px;right:32px;width:44px;height:44px;border-radius:50%;background:radial-gradient(circle,var(--gold) 50%,var(--gold-deep) 52%,var(--gold) 70%,var(--gold-deep));z-index:2}
.subline{top:376px;left:40px;right:40px;font:700 11px "Open Sans",Arial,sans-serif;color:var(--green);z-index:2}
.body-copy{top:394px;left:40px;right:40px;font:400 8.5px/1.45 "Open Sans",Arial,sans-serif;color:var(--text);z-index:2}
.body-copy p{margin-bottom:4px}
.contact{bottom:14px;left:24px;right:24px;height:24px;border-top:1px solid var(--line);border-bottom:1px solid var(--line);display:flex;justify-content:space-around;align-items:center;font:600 8px "Open Sans",Arial,sans-serif;color:var(--cream);z-index:2}
.contact span{display:flex;align-items:center;gap:4px}
.contact svg{width:9px;height:9px;fill:var(--green)}
.hero{top:38px;left:24px;width:200px;height:120px;background:linear-gradient(160deg,#7d9ab0,#4e3b26 60%,#2c1e12)}
.side-a{top:38px;left:232px;width:164px;height:56px;background:linear-gradient(135deg,#5a4a3a,#2a1e14)}
.side-b{top:102px;left:232px;width:164px;height:56px;background:linear-gradient(135deg,#b84a78,#4a2a1c)}
.pill{background:var(--green);color:#fff;font:700 8.5px "Open Sans",Arial,sans-serif;padding:3px 10px;border-radius:10px;z-index:2}
.pill-top{top:166px;left:50%;transform:translateX(-50%)}
.box{border:1px solid var(--line);background:var(--panel);padding:8px;z-index:2}
.box h3{font:700 10px "Open Sans",Arial,sans-serif;color:var(--gold);margin-bottom:6px}
.options{top:188px;left:24px;width:180px;height:150px}
.options table{width:100%;border-collapse:collapse;font-size:7.5px}
.options td{padding:3px 2px;border-bottom:1px solid rgba(201,162,58,.35)}
.options td:last-child{text-align:right;color:var(--green);font-weight:700}
.features{top:188px;left:212px;width:184px;height:150px}
.features ul{list-style:none;font-size:7.5px;line-height:1.35}
.features li{display:flex;gap:4px;margin-bottom:4px}
.features svg{flex:none;width:8px;height:8px;margin-top:1px}
.pill-mid{top:346px;left:50%;transform:translateX(-50%);white-space:nowrap}
.uses{top:370px;left:24px;width:220px;height:118px}
.use-grid{display:grid;grid-template-columns:1fr 1fr;gap:6px}
.use{display:flex;align-items:center;gap:5px;font-size:7.5px}
.use i{width:20px;height:20px;border-radius:50%;border:1px solid var(--green);display:block;flex:none}
.pricing{top:370px;left:254px;width:142px;height:118px;background:#fff;border:2px solid var(--gold);z-index:2;padding:6px}
.pricing span{font:700 9px "Open Sans",Arial,sans-serif;color:#333}
</style>
</head>
<body>
<div class="spread">
  <section class="page front">
    <div class="brand"><span class="brand-dot"></span><span class="brand-name">Brisk Meadow Builders</span></div>
    <span class="chain" style="left:90px"></span><span class="chain" style="left:328px"></span>
    <div class="photo shelf" role="img" aria-label="Bar shelf stocked with liquor bottles and glasses"></div>
    <div class="thumbs">
      <div class="thumb t1" role="img" aria-label="Patio Perch Lounge in a back yard"></div>
      <div class="thumb t2" role="img" aria-label="Lounge with solar panel roof"></div>
      <div class="thumb t3" role="img" aria-label="Friends gathered at the lounge"></div>
      <div class="thumb t4" role="img" aria-label="Lounge interior with TV mount"></div>
    </div>
    <p class="tagline">Turn your back yard into the ultimate entertainment<br>venue with the stunning</p>
    <h1 class="title">PATIO PERCH LOUNGE!</h1>
    <div class="seal"></div>
    <p class="subline">Entertain family &amp; friends in your very own back yard!</p>
    <div class="body-copy">
      <p>Available with or without solar and comes in a variety of colors. The Patio Perch Lounge measures 5' deep by 10' wide and is 9'-6" at its highest point.</p>
      <p>Constructed with treated 4x4's, primed then painted with Thornby Calder best exterior paint for years of care free enjoyment. Marlow Pendt Keystead shingles are dimensional, have a 25 year warranty and are rated for 150 mph winds!</p>
    </div>
    <div class="contact">
      <span><svg viewBox="0 0 10 10"><path d="M2 1l2 2-1 1.5c.7 1.3 1.5 2.1 2.5 2.5L7 6l2 2-1.5 1.5C4 9 1 6 .5 2.5z"/></svg>(555) 014-2290</span>
      <span><svg viewBox="0 0 10 10"><path d="M5 0a3.5 3.5 0 0 1 3.5 3.5C8.5 6 5 10 5 10S1.5 6 1.5 3.5A3.5 3.5 0 0 1 5 0zm0 2a1.5 1.5 0 1 0 0 3 1.5 1.5 0 0 0 0-3z"/></svg>418 Alder Row, Fenwick</span>
      <span>briskmeadowbuilders.com</span>
    </div>
  </section>

  <section class="page back">
    <div class="brand"><span class="brand-dot"></span><span class="brand-name">Brisk Meadow Builders</span></div>
    <div class="photo hero" role="img" aria-label="Patio Perch Lounge with bar counter and stools"></div>
    <div class="photo side-a" role="img" aria-label="Bar counter detail"></div>
    <div class="photo side-b" role="img" aria-label="Lounge painted in a bright color"></div>
    <span class="pill pill-top">Check Options</span>
    <div class="box options">
      <h3>Available Options</h3>
      <table>
        <tr><td>Solar Panel Kit</td><td>Add-on</td></tr>
        <tr><td>Color Choice</td><td>8 Options</td></tr>
        <tr><td>LED Lighting</td><td>Add-on</td></tr>
        <tr><td>Bar Stools</td><td>Set of 4</td></tr>
        <tr><td>Side Shelving</td><td>Add-on</td></tr>
      </table>
    </div>
    <div class="box features">
      <h3>Base Unit Features</h3>
      <ul>
        <li><svg viewBox="0 0 10 10"><path d="M1 5l3 3 5-6" stroke="#7cc242" stroke-width="2" fill="none"/></svg>Measures 5' deep by 10' wide, 9'-6" at its highest point</li>
        <li><svg viewBox="0 0 10 10"><path d="M1 5l3 3 5-6" stroke="#7cc242" stroke-width="2" fill="none"/></svg>Treated 4x4's, primed and painted with Thornby Calder exterior paint</li>
        <li><svg viewBox="0 0 10 10"><path d="M1 5l3 3 5-6" stroke="#7cc242" stroke-width="2" fill="none"/></svg>Marlow Pendt Keystead shingles, 25 year warranty, 150 mph winds</li>
        <li><svg viewBox="0 0 10 10"><path d="M1 5l3 3 5-6" stroke="#7cc242" stroke-width="2" fill="none"/></svg>TV Mount included. Shelves and TV are sold separately</li>
      </ul>
    </div>
    <span class="pill pill-mid">Available with or without solar and comes in a variety of colors</span>
    <div class="box uses">
      <h3>Use Cases</h3>
      <div class="use-grid">
        <div class="use"><i></i>Game Day Parties</div>
        <div class="use"><i></i>Family Cookouts</div>
        <div class="use"><i></i>Evening Gatherings</div>
        <div class="use"><i></i>Poolside Bar</div>
      </div>
    </div>
    <div class="pricing"><span>Pricing</span></div>
    <div class="contact">
      <span><svg viewBox="0 0 10 10"><path d="M2 1l2 2-1 1.5c.7 1.3 1.5 2.1 2.5 2.5L7 6l2 2-1.5 1.5C4 9 1 6 .5 2.5z"/></svg>(555) 014-2290</span>
      <span><svg viewBox="0 0 10 10"><path d="M5 0a3.5 3.5 0 0 1 3.5 3.5C8.5 6 5 10 5 10S1.5 6 1.5 3.5A3.5 3.5 0 0 1 5 0zm0 2a1.5 1.5 0 1 0 0 3 1.5 1.5 0 0 0 0-3z"/></svg>418 Alder Row, Fenwick</span>
      <span>briskmeadowbuilders.com</span>
    </div>
  </section>
</div>
</body>
</html>
```